IT Consulting Site Revamping for Marlune

I've put a skeleton together on my website, but realize I need some help (it's http://pilot.marlune-example.ca).
I've pulled together tidbits from other websites, but really need my site to be cleaned up, and really spruced up.
I primarily focus on the IT needs of small to medium size businesses, taking care of everything from their servers and networks down to their workstations.
I also want a page listing the vendors (and logos) that I work with including Quillsoft, Zentrix, Halvor, Brax, TL, RZO, VELK, Trevo, Gatemoor.
There should also be a simple form to get a quote that will email me.
The final design should communicate strength and reliability.
I would like this to be a fully functional website, that I can upload to Plumly Pages, with the same sort of pages that are existing on http://pilot.marlune-example.ca
Updates
Hey everyone,
Hi everyone,
Reason: Hi all,
There are some designers that would like to submit some new designs, so I'm extending the deadline.
Thanks,
Target Market(s)
Small to medium size business owners. This will primarily be males who work in the oil and gas industry.
Industry/Entity Type
Consulting
Look and feel
Each slider illustrates characteristics of the customer's brand and the style your logo design should communicate.

```html
<!DOCTYPE html>
<html lang="en">
<head>
<meta charset="utf-8">
<title>Marlune Solutions</title>
<link rel="stylesheet" href="https://fonts.googleapis.com/css2?family=Saira+Condensed:wght@400;500;600&family=PT+Sans:wght@400;700&display=swap">
<style>
:root{
  --blue:#2a7bc0;
  --blue-dark:#0d4f9a;
  --ink:#4a4a4a;
  --muted:#6b6b6b;
  --line:#d9dde2;
  --bg:#ffffff;
  --footer:#2d7ab9;
}
*{box-sizing:border-box;margin:0;padding:0}
html,body{width:1184px;height:1200px;overflow:hidden;background:var(--bg);font-family:"PT Sans",sans-serif;color:var(--ink)}
.page{position:relative;width:1184px;height:1200px}
.wrap{position:absolute;left:230px;width:726px}

.site-header{position:absolute;top:0;left:0;width:100%;height:106px;border-bottom:1px solid var(--line)}
.brand{position:absolute;left:232px;top:24px;display:flex;align-items:center;gap:14px}
.brand-mark{width:54px;height:54px;border-radius:50%;background:var(--blue)}
.brand-name{font-family:"Saira Condensed",sans-serif;font-weight:500;font-size:44px;color:var(--blue);line-height:1}
.contact-top{position:absolute;right:228px;top:50px;display:flex;gap:22px;font-size:11px;color:var(--muted);align-items:center}
.contact-top span{display:flex;align-items:center;gap:6px}

.main-nav{position:absolute;top:106px;left:0;width:100%;height:53px}
.main-nav ul{position:absolute;left:230px;width:726px;height:53px;list-style:none;display:flex;border-left:1px solid var(--line);border-right:1px solid var(--line)}
.main-nav li{height:53px;display:flex;align-items:center;justify-content:center;border-right:1px solid var(--line);font-family:"Saira Condensed",sans-serif;font-size:15px;color:var(--blue);text-transform:uppercase;gap:6px}
.main-nav li.w1{width:79px}.main-nav li.w2{width:98px}.main-nav li.w3{width:99px}.main-nav li.w4{width:121px}.main-nav li.w5{width:109px}
.search{margin-left:16px;margin-top:13px;width:190px;height:26px;border:1px solid #c7cfd8;border-radius:13px;display:flex;overflow:hidden}
.search span{flex:1;font-size:11px;color:var(--blue);padding:5px 13px}
.search i{width:32px;background:var(--blue);display:flex;align-items:center;justify-content:center}

.hero{position:absolute;top:159px;left:0;width:100%;height:267px;background:linear-gradient(90deg,#cfcfcf 0%,#8b8f96 14%,#3b3f48 30%,#6e5a4a 48%,#40444d 62%,#8b7a6c 78%,#2e3440 90%,#c9c9c9 100%);overflow:hidden}
.hero-person{position:absolute;left:672px;top:14px;width:160px;height:253px;background:linear-gradient(180deg,#d9b88d 0%,#b9a99a 35%,#7b7875 100%);border-radius:70px 70px 0 0}
.hero-title{position:absolute;left:292px;top:94px;font-family:"Saira Condensed",sans-serif;font-size:32px;color:#fff;letter-spacing:-.5px}
.hero-title b{font-weight:600}
.hero-text{position:absolute;left:292px;top:145px;width:360px;font-size:11px;line-height:15px;color:#eee}
.hero-arrow{position:absolute;top:108px}
.dots{position:absolute;left:566px;top:211px;display:flex;gap:6px}
.dots i{width:9px;height:9px;border-radius:50%;background:#eee;border:1px solid #bbb}
.dots i.on{background:var(--blue)}

.card{position:absolute;top:400px;width:220px;height:241px;background:#fff;border:1px solid var(--line);box-shadow:0 1px 3px rgba(0,0,0,.08);padding:14px 11px}
.card h3{font-family:"Saira Condensed",sans-serif;font-weight:400;font-size:23px;color:var(--blue);display:flex;align-items:center;gap:5px;text-transform:uppercase;line-height:1}
.card-photo{margin-top:13px;height:78px;border:1px solid #b8cde0}
.card p{margin-top:8px;font-size:9.5px;line-height:14px;color:var(--muted)}
.read-more{margin-top:13px;display:inline-flex;align-items:center;gap:8px;height:17px;border:1px solid #999;border-radius:9px;font-size:8px;padding-right:10px;color:#444}
.read-more i{width:17px;height:15px;border-radius:8px;background:#4d4d4d;display:flex;align-items:center;justify-content:center}

.questions{position:absolute;left:738px;top:400px;width:220px;height:241px;background:#fff;border:1px solid var(--line)}
.q-head{height:96px;background:linear-gradient(180deg,var(--blue) 0%,var(--blue-dark) 100%);display:flex;align-items:center;gap:12px;padding:0 27px;color:#fff}
.q-icon{width:46px;height:46px;border-radius:8px;background:#0b4585;display:flex;align-items:center;justify-content:center}
.q-head h4{font-family:"Saira Condensed",sans-serif;font-weight:400;font-size:21px;line-height:1}
.q-head p{font-size:9.5px;line-height:12px;margin-top:3px}
.q-row{height:48px;border-bottom:1px solid var(--line);display:flex;align-items:center;gap:12px;padding-left:20px;font-size:12.5px;color:#444}
.q-row:last-child{border-bottom:0}

.intro{top:660px}
.intro h2{font-family:"Saira Condensed",sans-serif;font-weight:400;font-size:23px;line-height:25px;color:var(--blue);text-transform:uppercase}
.intro .body{margin-top:16px}
.intro p{font-size:9.6px;line-height:12.6px;color:#5a5a5a;margin-bottom:12.3px}

.partners{top:1002px}
.partners h2{font-family:"Saira Condensed",sans-serif;font-weight:400;font-size:23px;color:var(--blue);padding-bottom:6px;border-bottom:1px solid var(--line)}
.partner-list{height:80px;border-bottom:1px solid var(--line);display:flex;align-items:center;justify-content:space-between;padding:0 2px}
.partner{font-family:"PT Sans",sans-serif;font-weight:700;font-size:15px;color:#3a3a3a;display:flex;align-items:center;gap:5px}
.partner i{width:12px;height:12px;border-radius:50%;background:#9a9a9a}

.site-footer{position:absolute;left:0;top:1146px;width:100%;height:54px;background:var(--footer);color:#fff;font-size:10px}
.site-footer .copy{position:absolute;left:258px;top:20px}
.site-footer nav{position:absolute;right:248px;top:20px;display:flex;gap:12px}
</style>
</head>
<body>
<div class="page">
  <header class="site-header">
    <div class="brand"><span class="brand-mark"></span><span class="brand-name">Marlune</span></div>
    <div class="contact-top">
      <span><svg width="8" height="14" viewBox="0 0 8 14"><path d="M6 1H4C2 1 1 3 1 7s1 6 3 6h2" fill="none" stroke="#777" stroke-width="1.6"/></svg>+0000 000 000</span>
      <span><svg width="16" height="11" viewBox="0 0 16 11"><rect x=".5" y=".5" width="15" height="10" fill="none" stroke="#777"/><path d="M.5 .5L8 6l7.5-5.5" fill="none" stroke="#777"/></svg>sales@marlune-example.ca</span>
    </div>
  </header>

  <nav class="main-nav">
    <ul>
      <li class="w1"><svg width="10" height="8" viewBox="0 0 10 8"><path d="M1 7C1 3 4 1 9 1 8 5 6 7 1 7z" fill="#2a7bc0"/></svg>Home</li>
      <li class="w2">Our Service</li>
      <li class="w3">About Us</li>
      <li class="w4">Our Products</li>
      <li class="w5">Contact Us</li>
      <li style="border:0"><div class="search"><span>search....</span><i><svg width="13" height="13" viewBox="0 0 13 13"><circle cx="5" cy="5" r="3.8" fill="none" stroke="#fff" stroke-width="1.6"/><path d="M8 8l4 4" stroke="#fff" stroke-width="2"/></svg></i></div></li>
    </ul>
  </nav>

  <section class="hero">
    <div class="hero-person" role="img" aria-label="Photo of a smiling businesswoman in a grey suit with arms crossed"></div>
    <h1 class="hero-title">A <b>MARLUNE SOLUTIONS</b> GOES HERE</h1>
    <p class="hero-text">There are many variations of passages of Lorem Ipsum available, but the majority have suffered a iteration in some form....</p>
    <svg class="hero-arrow" style="left:230px" width="30" height="56" viewBox="0 0 30 56"><path d="M28 2L3 28l25 26" fill="none" stroke="#2a7bc0" stroke-width="1.6"/></svg>
    <svg class="hero-arrow" style="left:926px" width="30" height="56" viewBox="0 0 30 56"><path d="M2 2l25 26L2 54" fill="none" stroke="#2a7bc0" stroke-width="1.6"/></svg>
    <div class="dots"><i></i><i class="on"></i><i></i><i></i></div>
  </section>

  <article class="card" style="left:230px">
    <h3><svg width="16" height="13" viewBox="0 0 16 13"><path d="M1 12C1 5 6 1 15 1 13 8 9 12 1 12z" fill="#2a7bc0"/></svg>Business</h3>
    <div class="card-photo" role="img" aria-label="Photo of a coffee cup on a newspaper with glasses" style="background:linear-gradient(180deg,#e8eef6,#9fb6d0)"></div>
    <p>Lorem Ipsum has been the industry's standard dummy text ever since the 1500s, when an unknown printer took a galley of type and scrambled it to make a type specimen book.</p>
    <span class="read-more"><i><svg width="5" height="6" viewBox="0 0 5 6"><path d="M0 0l5 3-5 3z" fill="#fff"/></svg></i>Read More</span>
  </article>

  <article class="card" style="left:484px">
    <h3><svg width="16" height="13" viewBox="0 0 16 13"><path d="M1 12C1 5 6 1 15 1 13 8 9 12 1 12z" fill="#2a7bc0"/></svg>Work Business</h3>
    <div class="card-photo" role="img" aria-label="Photo of a glass globe on blocks under a blue sky" style="background:linear-gradient(180deg,#1d5fb3,#8fb8e6 60%,#e6eef7)"></div>
    <p>Lorem Ipsum has been the industry's standard dummy text ever since the 1500s, when an unknown printer took a galley of type and scrambled it to make a type specimen book.</p>
    <span class="read-more"><i><svg width="5" height="6" viewBox="0 0 5 6"><path d="M0 0l5 3-5 3z" fill="#fff"/></svg></i>Read More</span>
  </article>

  <aside class="questions">
    <div class="q-head">
      <div class="q-icon"><svg width="24" height="24" viewBox="0 0 24 24"><path d="M4 20l2-6L17 3l4 4L10 18z M14 6l4 4" fill="none" stroke="#fff" stroke-width="1.6"/></svg></div>
      <div><h4>QUESTIONS?</h4><p>Need a quote?<br>Have a question? Aak us!</p></div>
    </div>
    <div class="q-row"><svg width="12" height="12" viewBox="0 0 12 12"><path d="M2 1l3 1-1 3 3 3 3-1 1 3-2 1C5 11 1 7 1 3z" fill="#999"/></svg>Call + (555) 010 - 2314</div>
    <div class="q-row"><svg width="12" height="9" viewBox="0 0 12 9"><rect x=".5" y=".5" width="11" height="8" fill="none" stroke="#999"/><path d="M.5 .5L6 5l5.5-4.5" fill="none" stroke="#999"/></svg>Send us an email</div>
    <div class="q-row"><svg width="10" height="12" viewBox="0 0 10 12"><rect x=".5" y=".5" width="9" height="11" fill="none" stroke="#999"/><rect x="2" y="2" width="6" height="2" fill="#999"/><path d="M2 6h1M5 6h1M2 8h1M5 8h1M2 10h1M5 10h1" stroke="#999"/></svg>Get a Quote</div>
  </aside>

  <section class="wrap intro">
    <h2>Small Business Information Technology Services<br>Easy, Affordable and Reliable.</h2>
    <div class="body">
      <p>Marlune Solutions is a computer solutions provider and IT consulting firm that supports a wide variety of local small businesses in the Calgary area primarily. Our company also provides IT services to businesses throughout Alberta on special projects.</p>
      <p>Marlune has been trusted for over the last 7 years by small business companies like yours. Whether you are looking for an ongoing computer support company, looking to outsource your small business computer work, or just looking for a computer company to help you solve a computer problem, Marlune is your right choice.</p>
      <p>We have a diversity of small business support solutions. We provide in office, over the phone, remote or drop-off computer technical support services to small business.</p>
      <p>Our computer technicians and network professionals understand that your business operations hinge on computer and network availability. Regardless if your business has one or many business locations, our preventive and ongoing business support solutions can help you keep all your computer systems running smoothly.</p>
      <p>Our computer business support services deliver unmatched reliability and expertise in computer networking, remote access, firewalls, VPNs and desktop services. Our clients enjoy that our small business support services are flexible, easy and affordable.</p>
      <p>Marlune has been recognised by many business owners for our dedication to delivering exceptional business computer support services and IT solutions. Our trained and experienced IT professionals deliver all day, and every day, rapid issue resolution, ongoing support, maintenance and stability that your business deserves and can depend upon.</p>
      <p>If you are a small business experiencing a computer or network problems or you are seeking ongoing technical support for your small business, contact us today for a free site survey and support analysis to help you find the right solution for your business.</p>
    </div>
  </section>

  <section class="wrap partners">
    <h2>OUR PARTNERS</h2>
    <div class="partner-list">
      <span class="partner">Quillsoft</span>
      <span class="partner">Trevo</span>
      <span class="partner">Halvor</span>
      <span class="partner"><i></i>Brax</span>
      <span class="partner">RZO</span>
      <span class="partner"><i></i>TL</span>
      <span class="partner">VELK</span>
      <span class="partner">Gatemoor</span>
      <span class="partner" style="color:#8a8a8a">Zentrix</span>
    </div>
  </section>

  <footer class="site-footer">
    <div class="copy"><b>© 2012, Marlune Solutions,</b> P.O. Box 0000, Fernvale, MA 00000</div>
    <nav><span>Home</span><span>|</span><span>About us</span><span>|</span><span>Contact us</span></nav>
  </footer>
</div>
</body>
</html>
```